Business Card Design Project

use presentation folder design and my logo and make 4 over 4 business cards

Industry/Entity Type

Business

Requirements
Must have
• use the design from my presentation folder and put my logo on it

Name
Title
phone
fax
email

```html
<!DOCTYPE html>
<html lang="en">
<head>
<meta charset="utf-8">
<title>Kindpath Counseling — Business Card</title>
<link rel="stylesheet" href="https://fonts.googleapis.com/css2?family=Arimo:wght@700&family=Tinos:wght@700&display=swap">
<style>
  :root {
    --brown: #7a3312;
    --slate: #7a8e8a;
    --label-grey: #596263;
    --pattern-tone: #a87651;
    --paper: #ffffff;
    --edge: #111111;
  }
  * { margin: 0; padding: 0; box-sizing: border-box; }
  html, body { width: 1200px; height: 1000px; overflow: hidden; background: var(--paper); }
  .sheet { position: relative; width: 1200px; height: 1000px; }

  .side-label {
    position: absolute;
    font-family: "Arimo", Arial, sans-serif;
    font-weight: 700;
    font-size: 62px;
    color: var(--label-grey);
    line-height: 1;
  }
  .side-label--front { left: 81px; top: 128px; }
  .side-label--back { left: 57px; top: 816px; }

  .card {
    position: absolute;
    border: 2px solid var(--edge);
    border-radius: 2px;
    overflow: hidden;
    background: var(--paper);
    font-family: "Tinos", "Times New Roman", serif;
    font-weight: 700;
  }
  .card--front { left: 404px; top: 44px; width: 756px; height: 436px; }
  .card--back { left: 401px; top: 532px; width: 759px; height: 436px; }

  .holder { position: absolute; left: 36px; top: 102px; width: 294px; text-align: center; }
  .holder__name { font-size: 31px; color: var(--brown); line-height: 1.1; }
  .holder__title { font-size: 23px; color: var(--slate); margin-top: 6px; }

  .brand {
    position: absolute; left: 438px; top: 88px;
    display: flex; align-items: center; gap: 16px;
  }
  .brand__dot { width: 40px; height: 40px; border-radius: 50%; background: var(--brown); }
  .brand__name { font-size: 40px; color: var(--brown); line-height: 1.05; }

  .contact { position: absolute; left: 14px; top: 238px; font-size: 20px; color: var(--brown); line-height: 30px; }
  .contact__key { color: var(--slate); }
  .contact__key--large { font-size: 24px; }

  .office { position: absolute; right: 14px; top: 243px; text-align: right; font-size: 20px; line-height: 29px; color: var(--brown); }
  .office__heading { color: var(--slate); }

  .footer-band { position: absolute; left: 0; bottom: 0; height: 58px; display: flex; width: 100%; }
  .footer-band__slate { width: 508px; background: var(--slate); }
  .footer-band__brown { flex: 1; background: var(--brown); }

  .back-pattern {
    position: absolute; inset: 0;
    background: radial-gradient(circle at 50% 50%, #85401c 0%, var(--brown) 75%);
  }
</style>
</head>
<body>
<main class="sheet">
  <p class="side-label side-label--front">Front</p>
  <p class="side-label side-label--back">Back</p>

  <section class="card card--front" aria-label="Business card front">
    <div class="holder">
      <p class="holder__name">Dorian Hallworth</p>
      <p class="holder__title">Founder / CEO</p>
    </div>

    <div class="brand">
      <span class="brand__dot"></span>
      <p class="brand__name">Kindpath<br>Counseling</p>
    </div>

    <div class="contact">
      <p><span class="contact__key contact__key--large">T:</span> 404.555.0182</p>
      <p><span class="contact__key">F:</span> 678.555.0137</p>
      <p><span class="contact__key">E:</span> KindpathCounseling@mail.com</p>
    </div>

    <div class="office">
      <p class="office__heading">Corporate Office</p>
      <p>4810 Larkfield Row N.W.</p>
      <p>Suite 210 Marbury GA 30199</p>
    </div>

    <div class="footer-band">
      <span class="footer-band__slate"></span>
      <span class="footer-band__brown"></span>
    </div>
  </section>

  <section class="card card--back" aria-label="Business card back">
    <div class="back-pattern" role="img" aria-label="Repeating brand pattern in light tan on deep brown"></div>
  </section>
</main>
</body>
</html>
```